Web site design for Brivolt Software (www.brivoltsoftware-example.com)

Need the design as well as the html for the website. The brief is given in the attached file.
If possible, would like to use pencil sketches instead of images to give a unique look to the site.
Target Market(s)
small Software product companies
Industry/Entity Type
Software
Coding
Coded - Design and coding required
Number of Pages Required
5+ page

```html
<!DOCTYPE html>
<html lang="en">
<head>
<meta charset="utf-8">
<title>Brivolt Software — Driven By Architecture</title>
<link href="https://fonts.googleapis.com/css2?family=Courier+Prime:wght@400;700&display=swap" rel="stylesheet">
<style>
  :root {
    --bar: #2f2f2f;
    --ink: #1d1d1d;
    --paper: #ffffff;
    --night: #000000;
    --graphite-pale: #f1f1f1;
    --graphite-light: #dcdcdc;
    --graphite-mid: #b4b4b4;
    --graphite-deep: #7d7d7d;
    --chalk: #5a5a5a;
  }
  * { margin: 0; padding: 0; box-sizing: border-box; }
  html, body { width: 1200px; height: 2260px; overflow: hidden; background: var(--paper); }
  body {
    position: relative;
    font-family: "Courier Prime", "Courier New", monospace;
    font-weight: 700;
    color: var(--ink);
  }

  .top-nav {
    position: absolute; left: 0; top: 0; width: 1200px; height: 56px;
    background: var(--bar);
    display: flex; justify-content: center; align-items: center; gap: 26px;
    padding-right: 40px;
  }
  .top-nav a {
    color: var(--paper); text-decoration: none; font-size: 13px;
    text-transform: uppercase;
  }

  .site-header { position: absolute; left: 0; top: 56px; width: 1200px; height: 77px; }
  .brand {
    position: absolute; left: 106px; top: 18px;
    display: flex; align-items: center; gap: 16px;
  }
  .brand-mark { width: 24px; height: 24px; background: var(--ink); }
  .brand-name { font-size: 36px; letter-spacing: 14px; color: var(--ink); text-transform: uppercase; }
  .tagline { position: absolute; right: 120px; top: 24px; font-size: 23px; }

  .hero {
    position: absolute; left: 0; top: 133px; width: 1200px; height: 361px;
    background: var(--night);
  }
  .hero-sketch {
    position: absolute; left: 135px; top: 51px; width: 394px; height: 281px;
    background: radial-gradient(ellipse at 50% 50%, var(--chalk) 0%, #2c2c2c 45%, var(--night) 78%);
  }
  .hero-quote {
    position: absolute; left: 619px; top: 94px; width: 462px;
    color: var(--paper); font-size: 20px; line-height: 32px;
  }
  .hero-quote cite {
    display: block; margin-top: 20px; font-style: normal; font-size: 14px; font-weight: 400;
  }

  .sketch {
    position: absolute;
    background: radial-gradient(ellipse at 50% 55%, var(--graphite-mid) 0%, var(--graphite-light) 40%, var(--graphite-pale) 65%, var(--paper) 85%);
  }
  .sketch-basilica { left: 619px; top: 565px; width: 459px; height: 269px; }
  .sketch-cloud { left: 141px; top: 1131px; width: 284px; height: 297px; }
  .sketch-gorge-bridge {
    left: 635px; top: 970px; width: 419px; height: 377px;
    background: linear-gradient(180deg, var(--graphite-pale) 0%, var(--graphite-light) 25%, var(--graphite-mid) 55%, var(--graphite-deep) 100%);
  }
  .sketch-cathedral { left: 619px; top: 1480px; width: 459px; height: 285px; }
  .sketch-river-bridge {
    left: 0; top: 1821px; width: 1200px; height: 369px;
    background: linear-gradient(180deg, var(--paper) 0%, var(--graphite-pale) 20%, var(--graphite-light) 45%, var(--graphite-mid) 75%, var(--graphite-light) 100%);
  }

  .section-title {
    position: absolute; left: 106px; top: 582px; font-size: 22px; letter-spacing: 2.4px;
  }
  .copy { position: absolute; font-size: 16.5px; line-height: 26px; }
  .copy p + p { margin-top: 16px; }
  .copy-intro { left: 106px; top: 645px; width: 480px; }
  .copy-cloud { left: 619px; top: 856px; width: 462px; }
  .copy-training { left: 619px; top: 1370px; width: 462px; }
  .copy-agile { left: 106px; top: 1503px; width: 480px; }

  .site-footer {
    position: absolute; left: 0; top: 2202px; width: 1200px; height: 58px;
    background: var(--bar); color: var(--paper);
  }
  .copyright { position: absolute; left: 106px; top: 19px; font-size: 16px; }
  .social { position: absolute; left: 937px; top: 22px; display: flex; gap: 30px; }
  .social span { width: 13px; height: 13px; border-radius: 50%; background: var(--paper); display: block; }
</style>
</head>
<body>
  <nav class="top-nav">
    <a href="#">Home</a><a href="#">Services</a><a href="#">About us</a><a href="#">Case studies</a>
    <a href="#">Accolades</a><a href="#">Giving back</a><a href="#">Partners</a><a href="#">Blog</a>
    <a href="#">Stories</a><a href="#">Contact us</a>
  </nav>

  <header class="site-header">
    <div class="brand"><span class="brand-mark"></span><span class="brand-name">Brivolt</span></div>
    <div class="tagline">Driven By Architecture</div>
  </header>

  <section class="hero">
    <div class="hero-sketch" role="img" aria-label="White pencil sketch of a blacksmith hammering at an anvil beside a forge"></div>
    <blockquote class="hero-quote">“Perfection is achieved not when there is nothing more to add, but when there is nothing left to take away.”
      <cite>-Henri Valmoret</cite>
    </blockquote>
  </section>

  <h2 class="section-title">BACKGROUND AND EXPERTISE</h2>

  <div class="copy copy-intro">
    <p>We are primarily server side programmers with expertise in large scale projects - be it Software development tools, Distributed software frameworks, Telecom and mediation software or Business intelligence.</p>
    <p>Over the years, we have been the trusted offshore product development partner for many startups and mid sized software product companies, and have built software products from scratch.</p>
    <p>We have built over 10 software products for startups all over the world. Best in class UI, and APIs have been designed and implemented by us. Often we take a core technology developed in a university, or an idea, and build a product around it.</p>
  </div>

  <div class="sketch sketch-basilica" role="img" aria-label="Pencil sketch of a domed basilica and colonnaded square"></div>
  <div class="copy copy-cloud">
    <p>We work in cloud, mobile apps, big data and analytics. We are now getting into predictive analytics, machine learning and AI.</p>
  </div>

  <div class="sketch sketch-cloud" role="img" aria-label="Pencil sketch of a cloud with arrows rising into and falling from it"></div>

  <div class="sketch sketch-gorge-bridge" role="img" aria-label="Engraving of a suspension bridge spanning a river gorge"></div>
  <div class="copy copy-training">
    <p>We conduct high end training in Scrum, clean code, and clean design inspired by Master Orwin. We conduct training in Corvel, and concurrency.</p>
  </div>

  <div class="copy copy-agile">
    <p>We have been associated with the leaders of the Agile movement, and have expertise implementing agile practices in Brivolt as well as other companies.</p>
    <p>We have expertise in Design and architectural interventions - taking a flawed product and breathing life back into it.</p>
  </div>

  <div class="sketch sketch-cathedral" role="img" aria-label="Pencil sketch of a domed cathedral among trees"></div>

  <div class="sketch sketch-river-bridge" role="img" aria-label="Engraving of a long suspension bridge over a river with boats"></div>

  <footer class="site-footer">
    <div class="copyright">Copyright © 2017 Brivolt Software.</div>
    <div class="social" aria-label="Social links"><span></span><span></span><span></span><span></span></div>
  </footer>
</body>
</html>
```